Psychotherapy Practice Needs Non-Corporate Stationary

I need an elegant design for letterhead, envelope, and note card for my psychotherapy private practice in Silicon Valley. I work with pre-teens, teens, and adults primarily with anxiety, stress, and depression.

Stationary should convey warmth and professionalism. I tend to like somewhat modern designs.

My business card is already done--attached here for reference.

Target Market(s)

Professionals of Silicon Valley, Academic Advisors at High Schools, Psychologists, Psychiatrists, Pediatricians, Directors of Human Resources, Community leaders

Industry/Entity Type

Psychology

Font styles to use
Serif

Requirements
Must have
• Logo attached--can use with or without the name included. Feel free to move the name to the right of the logo. I included all versions just in case. Colors to use should match or go with the logo (greens, maybe blues if they go), but can be somewhat softer than the bold greens and browns used. (Ex. more sage green vs. kelly green)
• Letterhead--please include the following:
• Marisol Quenneville, LMFT
• 318 Bellweather Lane, Suite 15
• Palo Alto, CA 94317
• 650-555-0187
• marisol@marisolquenneville.example
• marisolquenneville.example
• Envelope--please include:
• Marisol Quenneville, LMFT
• Palo Alto, CA 94317
• 650-555-0187
• marisolquenneville.example
• Note Card--please include:
• Marisol Quenneville, LMFT
• 650-555-0187
• marisolquenneville.example
Nice to have
• I'd love to see examples both with and without a logo watermark in the background. I especially like the watermark towards the lower right corner for the letterhead. I'd also like to see some versions of the letterhead with all contact info at the bottom.
Should not have
• It should not be corporate and should avoid harsh lines.

```html
<!DOCTYPE html>
<html lang="en">
<head>
<meta charset="utf-8">
<title>Marisol Quenneville, LMFT — Stationery</title>
<link rel="stylesheet" href="https://fonts.googleapis.com/css2?family=Cinzel:wght@500&family=EB+Garamond:wght@400&display=swap">
<style>
  :root {
    --backdrop: #bdaaf8;
    --paper: #ffffff;
    --mist-grey: #dde1df;
    --sage-light: #d3ebc0;
    --sage-pale: #e6f4da;
    --leaf-green: #5fcc00;
    --leaf-mark: #4fae1f;
    --label-top: #dcf83a;
    --label-bottom: #ffffff;
    --ink: #2a2a22;
    --fold-line: rgba(255,255,255,0.85);
  }
  * { margin: 0; padding: 0; box-sizing: border-box; }
  html, body { width: 1200px; height: 1200px; overflow: hidden; }
  body { background: var(--backdrop); position: relative; font-family: "EB Garamond", Georgia, serif; color: var(--ink); }

  .sheet { position: absolute; background: var(--paper); box-shadow: 0 6px 18px rgba(60,40,120,0.25); overflow: hidden; }
  .sheet .swoosh { position: absolute; inset: 0; width: 100%; height: 100%; }

  .brand { position: absolute; display: flex; align-items: center; gap: 8px; }
  .brand-dot { width: 34px; height: 34px; border-radius: 50%; background: var(--leaf-mark); flex: none; }
  .brand-name { font-family: "Cinzel", "Times New Roman", serif; font-weight: 500; color: var(--ink); letter-spacing: 0.02em; white-space: nowrap; }

  .contact { position: absolute; font-size: 11px; line-height: 1.35; color: var(--ink); white-space: nowrap; }

  /* Envelope front */
  .envelope-front { left: 40px; top: 40px; width: 540px; height: 290px; }
  .envelope-front .brand { left: 40px; top: 188px; }
  .envelope-front .brand-name { font-size: 14px; }
  .envelope-front .contact { left: 82px; top: 214px; }

  /* Envelope back */
  .envelope-back { position: absolute; left: 620px; top: 55px; width: 540px; height: 300px; background: var(--leaf-green); box-shadow: 0 6px 18px rgba(60,40,120,0.25); }
  .envelope-back .folds { position: absolute; inset: 0; width: 100%; height: 100%; }
  .seal-label { position: absolute; left: 170px; top: 0; width: 220px; height: 232px; background: linear-gradient(180deg, var(--label-top), var(--label-bottom)); }
  .seal-label .brand { left: 24px; top: 166px; }
  .seal-label .brand-dot { width: 38px; height: 38px; }
  .seal-label .brand-name { font-size: 12px; }

  /* Letterhead */
  .letterhead { left: 330px; top: 410px; width: 540px; height: 760px; }
  .letterhead .brand { left: 40px; top: 40px; }
  .letterhead .brand-name { font-size: 13px; }
  .letterhead .watermark { position: absolute; right: 50px; bottom: 120px; width: 150px; height: 150px; border-radius: 50%; background: var(--sage-pale); }
  .letterhead .contact { left: 40px; bottom: 26px; font-size: 10.5px; }
</style>
</head>
<body>

  <section class="sheet envelope-front" aria-label="Envelope front">
    <svg class="swoosh" viewBox="0 0 540 290" preserveAspectRatio="none" aria-hidden="true">
      <path d="M0,160 Q210,262 540,256 L540,290 L0,290 Z" fill="var(--mist-grey)"/>
      <path d="M230,290 C390,252 470,212 540,158 L540,290 Z" fill="var(--sage-pale)"/>
      <path d="M300,290 C430,258 495,225 540,190 L540,290 Z" fill="var(--sage-light)"/>
    </svg>
    <div class="brand">
      <span class="brand-dot"></span>
      <span class="brand-name">Marisol Quenneville, LMFT</span>
    </div>
    <p class="contact">318 Bellweather Lane, Suite 15, Palo Alto, CA 94317 | marisolquenneville.example<br>650-555-0187 | marisol@marisolquenneville.example</p>
  </section>

  <section class="envelope-back" aria-label="Envelope back">
    <svg class="folds" viewBox="0 0 540 300" preserveAspectRatio="none" aria-hidden="true">
      <path d="M0,158 L520,158 Q528,158 530,150 L540,100" fill="none" stroke="var(--fold-line)" stroke-width="1"/>
      <path d="M500,158 L500,270 Q500,280 510,282 L540,290" fill="none" stroke="var(--fold-line)" stroke-width="1"/>
      <path d="M0,270 Q60,275 62,240" fill="none" stroke="var(--fold-line)" stroke-width="1"/>
    </svg>
    <div class="seal-label">
      <div class="brand">
        <span class="brand-dot"></span>
        <span class="brand-name">Marisol Quenneville, LMFT</span>
      </div>
    </div>
  </section>

  <section class="sheet letterhead" aria-label="Letterhead">
    <svg class="swoosh" viewBox="0 0 540 760" preserveAspectRatio="none" aria-hidden="true">
      <path d="M0,640 Q240,712 540,696 L540,760 L0,760 Z" fill="var(--mist-grey)"/>
      <path d="M250,760 C410,730 490,690 540,630 L540,760 Z" fill="var(--sage-pale)"/>
      <path d="M330,760 C450,736 505,706 540,668 L540,760 Z" fill="var(--sage-light)"/>
    </svg>
    <div class="watermark" aria-hidden="true"></div>
    <div class="brand">
      <span class="brand-dot"></span>
      <span class="brand-name">Marisol Quenneville, LMFT</span>
    </div>
    <p class="contact">318 Bellweather Lane, Suite 15, Palo Alto, CA 94317 | marisolquenneville.example<br>650-555-0187 | marisol@marisolquenneville.example</p>
  </section>

</body>
</html>
```